Briefumschläge normal + DIN A4 Geschäftspapiere für eine zahnärztliche Abrechnungsfirma
Zielgruppe
Wir sind eine zahnärztliche Abrechnungsfirma. Bieten Dienstleistungen für den zahnärztlichen und zahntechnischen Bereich.
Aufgabenstellung
Die Gestaltung sollte modern, auffallend aber doch schlicht sein.
Möglichst in schwarz/ beige/ weiß.

```html
<!DOCTYPE html>
<html lang="de">
<head>
<meta charset="utf-8">
<title>Praxis Kontor – Briefbogen</title>
<link rel="stylesheet" href="https://fonts.googleapis.com/css2?family=Montserrat:wght@400;500&display=swap">
<style>
  :root {
    --ink: #141414;
    --text: #2b2b2b;
    --muted: #5a5a5a;
    --paper: #fbfbfa;
    --backdrop: #e8e3da;
    --sign-fill: #d9d6d1;
  }
  * { box-sizing: border-box; margin: 0; padding: 0; }
  html, body { width: 1200px; height: 1200px; overflow: hidden; }
  body {
    background: var(--backdrop);
    font-family: "Montserrat", Arial, sans-serif;
    color: var(--text);
    position: relative;
  }
  .letterhead {
    position: absolute;
    left: 210px; top: 50px;
    width: 780px; height: 1100px;
    background: var(--paper);
    box-shadow: 0 6px 24px rgba(0,0,0,.12);
    overflow: hidden;
  }
  .letterhead__band {
    position: absolute; left: 0; right: 0;
    background: var(--ink);
  }
  .letterhead__band--top { top: 0; height: 14px; }
  .letterhead__band--bottom { bottom: 0; height: 22px; }
  .brand {
    position: absolute; left: 70px; top: 130px;
  }
  .brand__name {
    font-size: 42px; font-weight: 500; color: var(--ink);
    line-height: 1;
  }
  .brand__tagline {
    margin-top: 10px;
    font-size: 13px; font-weight: 500; color: var(--ink);
  }
  .sender {
    position: absolute; left: 470px; top: 110px;
    font-style: normal;
    font-size: 10px; line-height: 1.5; color: var(--muted);
  }
  .sender__company { font-size: 13px; font-weight: 500; color: var(--ink); }
  .date {
    position: absolute; right: 80px; top: 215px;
    font-size: 10px; color: var(--muted);
  }
  .letter-body {
    position: absolute; left: 70px; top: 250px; width: 640px;
    font-size: 12px; line-height: 1.8;
  }
  .letter-body__greeting { margin-bottom: 16px; color: var(--ink); }
  .letter-body p + p { margin-top: 16px; }
  .signature {
    position: absolute; left: 70px; top: 700px;
    width: 170px; height: 44px;
    background: var(--sign-fill); border-radius: 4px;
  }
  .contact {
    position: absolute; left: 70px; top: 930px; width: 640px;
    display: flex; justify-content: space-between;
    font-size: 10px; line-height: 1.6; color: var(--muted);
  }
  .contact__item { display: flex; align-items: center; gap: 12px; }
  .contact__icon { width: 20px; height: 20px; flex: none; }
</style>
</head>
<body>
  <main class="letterhead">
    <div class="letterhead__band letterhead__band--top"></div>
    <div class="letterhead__band letterhead__band--bottom"></div>

    <header class="brand">
      <div class="brand__name">Praxis Kontor</div>
      <div class="brand__tagline">Abrechnungsservice für Zahnarztpraxen</div>
    </header>

    <address class="sender">
      <div class="sender__company">Company Name</div>
      <div>Lindenallee 12, 50667 Köln</div>
      <div>Deutschland</div>
    </address>

    <div class="date">3 February 2020</div>

    <section class="letter-body">
      <div class="letter-body__greeting">Hello,</div>
      <p>Vielen Dank für Ihr Vertrauen in unsere Arbeit. Wir übernehmen die Abrechnung Ihrer Praxis zuverlässig, schnell und transparent. So bleibt Ihnen mehr Zeit für Ihre Patienten und das Team.</p>
      <p>Unser Team prüft jede Leistung sorgfältig und achtet auf korrekte Gebührenordnungen. Offene Fragen klären wir direkt mit Ihnen und den Kostenträgern. Monatliche Berichte zeigen Ihnen jederzeit den aktuellen Stand Ihrer Forderungen.</p>
      <p>Auch für zahntechnische Labore bieten wir passende Lösungen an. Gerne stellen wir Ihnen unser Angebot in einem persönlichen Gespräch vor.</p>
      <p>Unsere Mitarbeiter verfügen über langjährige Erfahrung in der zahnärztlichen Verwaltung. Dadurch erkennen wir Fehler früh und sichern Ihre Einnahmen dauerhaft ab.</p>
      <p>Wir freuen uns auf die Zusammenarbeit mit Ihnen. Mit freundlichen Grüßen</p>
    </section>

    <div class="signature" role="img" aria-label="Handschriftliche Unterschrift"></div>

    <footer class="contact">
      <div class="contact__item">
        <svg class="contact__icon" viewBox="0 0 20 20" aria-hidden="true">
          <circle cx="10" cy="10" r="9" fill="#141414"/>
          <g fill="none" stroke="#fbfbfa" stroke-width="1.1">
            <ellipse cx="10" cy="10" rx="4" ry="8.5"/>
            <line x1="1.5" y1="10" x2="18.5" y2="10"/>
            <line x1="3" y1="6" x2="17" y2="6"/>
            <line x1="3" y1="14" x2="17" y2="14"/>
          </g>
        </svg>
        <div>www.praxiskontor.de<br>www.praxiskontor-abrechnung.de</div>
      </div>
      <div class="contact__item">
        <svg class="contact__icon" viewBox="0 0 20 20" aria-hidden="true">
          <path d="M5 2 L8 2 L9.5 6 L7.5 7.5 C8.5 9.8 10.2 11.5 12.5 12.5 L14 10.5 L18 12 L18 15 C18 16.7 16.7 18 15 18 C8.4 18 2 11.6 2 5 C2 3.3 3.3 2 5 2 Z" fill="#141414"/>
        </svg>
        <div>+49 221 4455 60<br>+49 221 4455 61</div>
      </div>
      <div class="contact__item">
        <svg class="contact__icon" viewBox="0 0 20 20" aria-hidden="true">
          <rect x="1" y="4" width="18" height="12" fill="#141414"/>
          <polyline points="1,4 10,11 19,4" fill="none" stroke="#fbfbfa" stroke-width="1.2"/>
        </svg>
        <div>kontakt@praxiskontor.de<br>info@praxiskontor.de</div>
      </div>
    </footer>
  </main>
</body>
</html>
```